Powerpoint master slide deck for power point presentation by members of my company

To design a master slide deck for powerpoint presentation for a Orthopaedic Clinic Based in Singapore

```html
<!DOCTYPE html>
<html lang="en">
<head>
<meta charset="utf-8">
<title>Stride Joint Clinic – Master Slide Deck</title>
<link rel="stylesheet" href="https://fonts.googleapis.com/css2?family=Poppins:ital,wght@0,400;0,500;0,600;0,700;1,400;1,500&display=swap">
<style>
:root{
  --teal:#3fa59d;
  --teal-dark:#2f7f80;
  --navy:#1f2f45;
  --ink:#2b2b2b;
  --grey-bg:#ebebed;
  --white:#ffffff;
  --aqua:#9ff3ec;
  --mint:#6fd3c7;
}
*{box-sizing:border-box;margin:0;padding:0}
html,body{width:1200px;height:3645px;overflow:hidden;background:#fff;font-family:'Poppins',sans-serif;color:var(--ink)}
.slide{position:absolute;left:99px;width:1000px;height:562px;overflow:hidden}
.abs{position:absolute}

/* Title slide */
.slide-title{top:56px}
.slide-title .photo{position:absolute;inset:0;background:linear-gradient(100deg,#18263a 0%,#23344c 45%,#4a5b6d 75%,#7d8996 100%)}
.brand{position:absolute;display:flex;align-items:center;gap:14px;font-weight:600;letter-spacing:2px}
.brand .mark{width:40px;height:40px;background:var(--teal)}
.slide-title .brand{left:28px;top:108px;color:var(--white);font-size:36px}
.slide-title h1{position:absolute;left:28px;top:208px;color:var(--white);font-size:46px;font-weight:700;line-height:58px}
.slide-title .mission{position:absolute;left:28px;top:338px;width:560px;color:var(--mint);font-style:italic;font-size:25px;line-height:39px}

/* About */
.slide-about{top:647px}
.slide-about .photo{position:absolute;left:0;top:0;width:560px;height:562px;background:linear-gradient(135deg,#4e6a66 0%,#3a5553 60%,#2e4443 100%)}
.slide-about svg.panel{position:absolute;left:0;top:0}
.slide-about .text{position:absolute;left:549px;top:50px;width:430px;color:var(--white)}
.slide-about h2{font-size:42px;font-weight:700;line-height:52px}
.slide-about .sub{font-size:30px;font-style:italic;line-height:41px;margin-top:14px}
.slide-about p{font-size:20px;line-height:36.5px;margin-top:22px}

/* Services */
.slide-services{top:1241px;background:var(--grey-bg)}
.center-title{position:absolute;left:0;width:100%;text-align:center;font-weight:700;color:var(--ink)}
.slide-services .center-title{top:34px;font-size:40px}
.slide-services .lead{position:absolute;top:92px;width:100%;text-align:center;font-size:19.5px}
.card{position:absolute;width:196px;height:174px}
.card .pic{height:129px}
.card .label{height:45px;background:var(--teal);color:var(--white);font-weight:600;font-size:16px;display:flex;align-items:center;justify-content:center;text-align:center;line-height:16px}

/* Why */
.slide-why{top:1833px}
.slide-why .photo{position:absolute;inset:0;background:linear-gradient(120deg,#2c4a66 0%,#2b6a74 50%,#2d7775 100%)}
.slide-why .center-title{top:38px;font-size:42px;color:var(--white)}
.slide-why .intro{position:absolute;top:100px;width:100%;text-align:center;color:var(--white);font-size:20px;line-height:32.5px}
.divider{position:absolute;left:14px;right:14px;top:283px;height:1px;background:rgba(255,255,255,.55)}
.divider span{position:absolute;left:50%;top:-17px;transform:translateX(-50%);padding:0 14px;background:#2a5f6e;color:var(--white);font-weight:700;font-size:23px;line-height:34px;white-space:nowrap}
.benefit{position:absolute;width:420px;color:var(--white);font-size:20px;line-height:32px;padding-left:70px}
.benefit::before{content:"»";position:absolute;left:30px;top:-2px;font-size:24px;font-weight:700}
.benefit.right{padding-left:39px}
.benefit.right::before{left:0}

/* Team */
.slide-team{top:2430px;background:var(--grey-bg)}
.slide-team .center-title{top:36px;font-size:40px}
.headshot{position:absolute;width:254px;height:251px;background:linear-gradient(180deg,#23324a 0%,#16223a 100%)}
.bio{position:absolute;width:356px;background:var(--white);padding:12px 14px}
.bio h3{font-size:24px;font-weight:700;line-height:30px}
.bio .role{font-size:14px;color:var(--teal);line-height:20px}
.bio p{font-size:11.5px;line-height:19.8px;margin-top:8px;color:#333}

/* Closing */
.slide-close{top:3029px;background:radial-gradient(ellipse at 50% 60%,#e9fdfb 0%,#bff8f2 55%,var(--aqua) 100%)}
.slide-close .brand{left:0;width:100%;justify-content:center;top:122px;color:var(--teal-dark);font-size:48px;letter-spacing:3px;font-weight:500}
.slide-close .brand .mark{width:54px;height:54px}
.slide-close .thanks{top:196px;font-size:60px}
.slide-close .more{position:absolute;top:268px;width:100%;text-align:center;font-size:21px;font-weight:500}
.contact{position:absolute;display:flex;gap:16px}
.contact .icon{width:44px;height:44px;flex:none;margin-top:0}
.contact h4{font-size:22px;font-weight:600;line-height:30px}
.contact .val{font-size:22px;line-height:30px}
.contact.small .val{font-size:19px}
</style>
</head>
<body>

<section class="slide slide-title">
  <div class="photo" role="img" aria-label="Photo of a surgeon in a white coat explaining a knee joint model to a patient"></div>
  <div class="brand"><span class="mark"></span>STRIDE JOINT</div>
  <h1>Singapore’s Hip &amp;<br>Knee Specialist</h1>
  <p class="mission">"Our mission is to promote individualised care that meets the needs and goals of every patient."</p>
</section>

<section class="slide slide-about">
  <div class="photo" role="img" aria-label="Portrait of the two clinic doctors, a woman seated and a man standing"></div>
  <svg class="panel" width="1000" height="562" viewBox="0 0 1000 562" aria-hidden="true">
    <path d="M500 0 H1000 V562 H430 C540 470 470 330 520 220 C560 130 530 60 500 0 Z" fill="#3fa59d"/>
  </svg>
  <div class="text">
    <h2>About Our Clinic</h2>
    <div class="sub">Your Trusted Orthopaedic Clinic in Singapore</div>
    <p>Medical treatment can often cause excessive anxiety and uncertainty. Our friendly team relentlessly focuses on prioritising all our patients' well-being. From common pains in the elderly and young to sport-related injuries, we specialise in treating various types of orthopaedic conditions.</p>
  </div>
</section>

<section class="slide slide-services">
  <h2 class="center-title">What We Do</h2>
  <p class="lead">Our doctors provide dedicated care for both chronic and complex orthopaedic conditions.</p>
  <div class="card" style="left:55px;top:150px"><div class="pic" role="img" aria-label="Hands holding a painful knee" style="background:linear-gradient(135deg,#e9e4e0,#cfc6c0)"></div><div class="label">Knee Evaluation</div></div>
  <div class="card" style="left:287px;top:150px"><div class="pic" role="img" aria-label="Surgeon performing knee arthroscopy" style="background:linear-gradient(135deg,#b9cde0,#7c9cbd)"></div><div class="label">Meniscus Repair</div></div>
  <div class="card" style="left:517px;top:150px"><div class="pic" role="img" aria-label="Surgical team in operating theatre" style="background:linear-gradient(135deg,#5f8fb8,#2f5b86)"></div><div class="label">ACL Tear &amp;<br>Reconstruction</div></div>
  <div class="card" style="left:748px;top:150px"><div class="pic" role="img" aria-label="Knee joint anatomy model" style="background:linear-gradient(135deg,#eef1f3,#c5d6dd)"></div><div class="label">Cartilage Repair</div></div>
  <div class="card" style="left:55px;top:342px"><div class="pic" role="img" aria-label="Pelvis with hip implant" style="background:linear-gradient(135deg,#efe7d0,#bfa76a)"></div><div class="label">Hip Replacement</div></div>
  <div class="card" style="left:287px;top:342px"><div class="pic" role="img" aria-label="Person holding a painful hip" style="background:linear-gradient(135deg,#b77a8e,#6d2c45)"></div><div class="label">Hip Evaluation</div></div>
  <div class="card" style="left:517px;top:342px"><div class="pic" role="img" aria-label="Cross sections of femur bones" style="background:linear-gradient(135deg,#f1efe6,#d6d0b6)"></div><div class="label">Bone Wellness</div></div>
  <div class="card" style="left:748px;top:342px"><div class="pic" role="img" aria-label="Row of knee implant models" style="background:linear-gradient(135deg,#8fb5ad,#3f6f6a)"></div><div class="label">Knee Replacement</div></div>
</section>

<section class="slide slide-why">
  <div class="photo" role="img" aria-label="Surgical team at work in an operating theatre, tinted teal"></div>
  <h2 class="center-title">Why Choose Us?</h2>
  <p class="intro">We take pride in our patient-centred and honest approach, offering services that are<br>sustainable and affordable for our clients.<br>Both our doctors are Medisave-accredited, and patients may use their Medisave<br>for eligible procedures, consultations, and medications.</p>
  <div class="divider"><span>Key Benefits Include</span></div>
  <p class="benefit" style="left:0;top:326px">Our initial consultation begins at $160.50 (w. GST).</p>
  <p class="benefit" style="left:0;top:404px;line-height:25.5px">We collaborate with many insurance providers, including corporate, which ensures seamless and potentially cashless visits to the clinic.</p>
  <p class="benefit right" style="left:524px;top:326px;width:460px">Our clinic is on the panel of most Integrated Shield Plans, Singapore.</p>
  <p class="benefit right" style="left:524px;top:402px;width:460px">We adhere to Ministry of Health Singapore fee benchmarks.</p>
</section>

<section class="slide slide-team">
  <h2 class="center-title">Meet Our Team</h2>
  <div class="headshot" style="left:14px;top:126px" role="img" aria-label="Portrait of Dr Marcus Teo"></div>
  <div class="bio" style="left:117px;top:318px;height:203px">
    <h3>Dr Marcus Teo</h3>
    <div class="role">Orthopaedic Surgery Specialist</div>
    <p>Dr Marcus Teo is an orthopaedic surgeon with subspecialty training in primary and complex hip and knee replacements. He is able to provide consult on hip and knee surgery, in particular the painful total knee, prosthetic joint infection, revision hip and knee surgeries, and periprosthetic fracture.</p>
  </div>
  <div class="headshot" style="left:524px;top:126px" role="img" aria-label="Portrait of Dr Lim Wei Ling"></div>
  <div class="bio" style="left:627px;top:302px;height:219px;padding-top:28px">
    <h3>Dr Lim Wei Ling</h3>
    <div class="role">Orthopaedic Surgery Specialist</div>
    <p>Dr Lim is an orthopaedic surgeon with subspecialty training in hip and knee surgery, making her the first female hip and knee surgeon in Singapore. She is also a Visiting Consultant to Northgate Medical Centre, and is able to provide consult to a wide range of orthopaedic conditions.</p>
  </div>
</section>

<section class="slide slide-close">
  <div class="brand"><span class="mark"></span>STRIDE JOINT</div>
  <h2 class="center-title thanks">Thank You</h2>
  <p class="more">For more info, please visit</p>
  <div class="contact" style="left:120px;top:340px">
    <svg class="icon" viewBox="0 0 44 44" aria-hidden="true"><circle cx="22" cy="22" r="20" fill="none" stroke="#3fa59d" stroke-width="2"/><path d="M13 16 L19 14 L25 16 L31 14 V28 L25 30 L19 28 L13 30 Z" fill="#3fa59d"/></svg>
    <div><h4>Address</h4><div class="val">Harbourview Medical<br>Centre,<br>12 Example Road,<br>#05-10/12, Singapore 000000.</div></div>
  </div>
  <div class="contact" style="left:566px;top:340px">
    <svg class="icon" viewBox="0 0 44 44" aria-hidden="true"><circle cx="22" cy="22" r="20" fill="none" stroke="#3fa59d" stroke-width="2"/><path d="M16 13 L20 13 L22 18 L19 20 C20 23 22 25 25 26 L27 23 L31 25 L31 29 C23 30 14 21 16 13 Z" fill="#3fa59d"/></svg>
    <div><h4>Phone</h4><div class="val">+65 8000 1234</div></div>
  </div>
  <div class="contact small" style="left:566px;top:418px">
    <svg class="icon" viewBox="0 0 44 44" aria-hidden="true"><circle cx="22" cy="22" r="20" fill="none" stroke="#3fa59d" stroke-width="2"/><rect x="12" y="15" width="20" height="14" rx="2" fill="#3fa59d"/><path d="M12 16 L22 23 L32 16" fill="none" stroke="#fff" stroke-width="1.6"/></svg>
    <div><h4>Email</h4><div class="val">hello@stridejoint.com.sg</div></div>
  </div>
</section>

</body>
</html>
```